BRD business cards Dr. Martin Velk

I need a business card designed for our dental office. We are a "general dental" practice.
Looking for a clean, professional but not too fancy design with our logo and contact information required.
front of card is information/standard business card, backside is appt reminder with lines for date and time of appt
doctors name: Dr. Martin Velk DMD
office name: Velk Family Dental
address: 4827 E Tolland Ave Brenwick Springs, FL 30999
phone: 555-555-0173
Dentistry
Office name, Doctor name, address, phone number...etc
- White/off white base color, blue and or black lettering

```html
<!DOCTYPE html>
<html lang="en">
<head>
<meta charset="utf-8">
<title>Velk Family Dental – Business Cards</title>
<link href="https://fonts.googleapis.com/css2?family=Marcellus+SC&display=swap" rel="stylesheet">
<style>
  :root {
    --page-bg: #e9e9e9;
    --card-white: #f7f7f7;
    --band-grey: #d9d9da;
    --ink: #141414;
    --ink-soft: #2a2a2a;
  }
  * { box-sizing: border-box; margin: 0; padding: 0; }
  html, body {
    width: 1200px; height: 900px; overflow: hidden;
    background: var(--page-bg);
    font-family: "Marcellus SC", "Times New Roman", serif;
    color: var(--ink);
  }
  .sheet { position: relative; width: 1200px; height: 900px; }
  .card {
    position: absolute; left: 250px; width: 700px; height: 400px;
    background: var(--card-white);
    box-shadow: 0 10px 30px rgba(0,0,0,.12);
    overflow: hidden;
  }
  .card--front { top: 40px; }
  .card--back { top: 460px; }
  .card__art { position: absolute; inset: 0; width: 100%; height: 100%; }
  .card__content { position: absolute; inset: 0; }

  /* Front */
  .brand {
    position: absolute; left: 0; right: 0; top: 70px;
    display: flex; flex-direction: column; align-items: center; gap: 6px;
  }
  .brand__mark {
    width: 46px; height: 46px; border-radius: 50%;
    border: 3px solid var(--ink);
  }
  .brand__name {
    font-size: 30px; letter-spacing: 2px; padding: 0 10px 4px;
    border-bottom: 2px solid var(--ink);
  }
  .brand__sub { font-size: 15px; letter-spacing: 9px; margin-top: -2px; }
  .doctor { position: absolute; left: 44px; top: 210px; }
  .doctor__name { font-size: 26px; letter-spacing: 1px; }
  .doctor__phone { font-size: 18px; margin-top: 4px; color: var(--ink-soft); }
  .address {
    position: absolute; left: 420px; top: 222px;
    display: flex; gap: 8px; font-size: 19px; line-height: 1.25; color: var(--ink-soft);
  }
  .address__icon { width: 16px; height: 22px; flex: none; margin-top: 1px; }

  /* Back */
  .back-title {
    position: absolute; left: 0; right: 0; top: 78px; text-align: center;
    font-size: 36px; letter-spacing: 1.5px; font-weight: 400;
  }
  .back-mark {
    position: absolute; left: 325px; top: 160px;
    width: 50px; height: 50px; border-radius: 50%; background: var(--ink);
  }
  .appt-label { position: absolute; left: 54px; top: 196px; font-size: 17px; letter-spacing: 1px; }
  .field { position: absolute; font-size: 16px; letter-spacing: 1px; }
  .field--date { left: 54px; top: 250px; }
  .field--time { left: 420px; top: 318px; }
  .field-line { position: absolute; left: 54px; right: 40px; height: 1.5px; background: var(--ink); }
  .field-line--date { top: 300px; }
  .field-line--time { top: 348px; }
</style>
</head>
<body>
<main class="sheet">

  <section class="card card--front" aria-label="Business card front">
    <svg class="card__art" viewBox="0 0 700 400" preserveAspectRatio="none" aria-hidden="true">
      <path d="M0 40 C 200 150, 500 190, 700 195 L700 370 C 520 300, 260 280, 0 290 Z" fill="var(--band-grey)"/>
      <path d="M0 30 C 60 70, 110 100, 170 118 C 110 96, 55 70, 0 46 Z" fill="var(--ink)"/>
      <path d="M460 300 C 560 318, 640 340, 700 372 L700 380 C 630 346, 560 326, 460 300 Z" fill="var(--ink)"/>
    </svg>
    <div class="card__content">
      <div class="brand">
        <span class="brand__mark"></span>
        <span class="brand__name">Velk Family</span>
        <span class="brand__sub">Dental</span>
      </div>
      <div class="doctor">
        <p class="doctor__name">Dr. Martin Velk DMD</p>
        <p class="doctor__phone">Ph: 555-555-0173</p>
      </div>
      <div class="address">
        <svg class="address__icon" viewBox="0 0 16 22" aria-hidden="true">
          <path d="M8 0C3.6 0 0 3.4 0 7.8 0 13.6 8 22 8 22s8-8.4 8-14.2C16 3.4 12.4 0 8 0z" fill="var(--ink)"/>
          <circle cx="8" cy="7.8" r="3" fill="var(--card-white)"/>
        </svg>
        <p>4827 E Tolland Ave<br>Brenwick Springs,<br>FL 30999</p>
      </div>
    </div>
  </section>

  <section class="card card--back" aria-label="Appointment reminder card">
    <svg class="card__art" viewBox="0 0 700 400" preserveAspectRatio="none" aria-hidden="true">
      <path d="M0 0 H700 V250 C 560 200, 420 175, 300 170 C 180 165, 80 150, 0 110 Z" fill="var(--band-grey)"/>
      <path d="M0 104 C 40 130, 90 150, 150 162 C 90 146, 40 126, 0 116 Z" fill="var(--ink)"/>
      <path d="M560 215 C 620 240, 665 262, 700 290 L700 300 C 660 270, 615 246, 560 215 Z" fill="var(--ink)"/>
    </svg>
    <div class="card__content">
      <h2 class="back-title">Velk Family Dental</h2>
      <span class="back-mark"></span>
      <p class="appt-label">Appointment</p>
      <p class="field field--date">Date</p>
      <p class="field field--time">Time</p>
      <span class="field-line field-line--date"></span>
      <span class="field-line field-line--time"></span>
    </div>
  </section>

</main>
</body>
</html>
```